Webbanner-Design für Versicherungsmakler
Zielgruppe
Wir führen eine ganzheitliche Betrachtung der individuellen finanziellen Situation des Kunden durch und erstellen auf dieser Basis ein persönliches Finanzkonzept. Wir haben uns spezialisiert auf die Beratung von Berufsunfähigkeitsversicherungen und der Altersvorsorge.
Aufgabenstellung
Es sollen Banner für Facebook-Seiten und Facebook-Werbeanzeigen erstellt werden. Sie stellen modern und ansprechend gestaltet sein. Es soll eine Interaktion beim Kunden angeregt werden. Das heißt, die Banner sollten entsprechend interessent gestaltet sein und neugierig machen.
Banner 1: Erstellung eines Versicherungsvergleichs
- Kunde soll aufgerufen werden sich einen Versicherungsvergleich erstellen zu lassen.
- Das Logo und der Weblink www.veltrama.de muss verwendet werden.
- Logo-Farben nutzen.
- Das Profilbild kann verwendet werden.
- Es soll auf eine Ersparnis mit bis zu 200 Euro im Jahr aufmerksam gemacht werden.
- Vorteil für den Kunden: richtige Versicherung finden, nur soviel bezahlen wie nötig.
Banner 2: Erstellung eines persönlichen Finanzkonzeptes
- Kunde soll aufgerufen werden sich ein Finanzkonzept erstellen zu lassen.
- Finanzkonzept beinhaltet alle Versicherungssparten, zeigt Versorungslücken bzw. eine Überversorgung auf. Gemeinsam ordnen wir dann mit dem Kunden seine Finanzsituation.
- Vorteil für den Kunden: Ganzheitliche Betrachtung der Finanzsituation, Nie mehr Kündigungstermine verpassen, richtige Versicherung finden, nur soviel bezahlen wie nötig.
18 - 99 Jahre
Alle Gehalts- und Bevölkerungsschichten
Grafiken/Gestaltung
Sie können unser Logo und das Profil-Bild benutzen, wenn sie zu eurem Design passt, ansonsten fügen bitte auf jedenfall eigene Grafiken (Lizenz muss vorhanden sein) ein.
Bitte Logo-Farben nutzen!
Format
- 1200x627px
- 470x264px

```html
<!DOCTYPE html>
<html lang="de">
<head>
<meta charset="utf-8">
<title>Veltrama Finance Consulting – Persönliches Finanzkonzept</title>
<link href="https://fonts.googleapis.com/css2?family=Montserrat:wght@400;500;600;700&display=swap" rel="stylesheet">
<style>
  :root {
    --brand-red: #d0212b;
    --brand-grey: #55575c;
    --text-light: #ffffff;
    --photo-warm: #b98579;
    --photo-deep: #8e5a52;
    --photo-mist: #d9d3d6;
    --overlay-left: #b9b6c0;
  }
  * { margin: 0; padding: 0; box-sizing: border-box; }
  html, body {
    width: 1200px;
    height: 627px;
    overflow: hidden;
    background: #ffffff;
  }
  .banner {
    position: relative;
    width: 1200px;
    height: 627px;
    overflow: hidden;
    font-family: "Montserrat", Arial, sans-serif;
  }
  .banner__photo {
    position: absolute;
    inset: 0;
    background:
      radial-gradient(ellipse 320px 420px at 960px 330px, rgba(120, 110, 112, 0.55), transparent 70%),
      linear-gradient(160deg, var(--photo-mist) 0%, var(--photo-warm) 45%, var(--photo-deep) 100%);
  }
  .banner__fade {
    position: absolute;
    inset: 0;
    background: linear-gradient(90deg,
      rgba(185, 182, 192, 0.95) 0%,
      rgba(190, 184, 192, 0.85) 35%,
      rgba(200, 190, 195, 0.35) 60%,
      rgba(200, 190, 195, 0) 75%);
  }
  .brand {
    position: absolute;
    left: 62px;
    top: 52px;
  }
  .brand__name {
    display: block;
    color: var(--brand-red);
    font-weight: 500;
    font-size: 54px;
    line-height: 1;
    letter-spacing: 1px;
  }
  .brand__tagline {
    display: block;
    margin-top: 14px;
    color: var(--brand-grey);
    font-weight: 400;
    font-size: 19px;
    letter-spacing: 0.3px;
  }
  .headline {
    position: absolute;
    left: 60px;
    top: 192px;
    color: var(--text-light);
    font-weight: 700;
    font-size: 37px;
    line-height: 51px;
    letter-spacing: 1px;
    text-transform: uppercase;
  }
  .benefits {
    position: absolute;
    left: 60px;
    top: 320px;
    list-style: none;
  }
  .benefits__item {
    display: flex;
    align-items: center;
    height: 38.5px;
    color: var(--text-light);
    font-weight: 500;
    font-size: 19px;
    letter-spacing: 0.6px;
    text-transform: uppercase;
  }
  .benefits__tick {
    width: 22px;
    height: 22px;
    margin-right: 9px;
    flex: none;
  }
  .cta {
    position: absolute;
    left: 61px;
    top: 465px;
    width: 274px;
    height: 50px;
    border-radius: 25px;
    background: var(--brand-red);
    color: var(--text-light);
    font-weight: 600;
    font-size: 18px;
    letter-spacing: 0.6px;
    display: flex;
    align-items: center;
    justify-content: center;
    text-decoration: none;
  }
  .web-address {
    position: absolute;
    left: 56px;
    top: 566px;
    color: var(--text-light);
    font-weight: 600;
    font-size: 18px;
    letter-spacing: 0.6px;
  }
</style>
</head>
<body>
  <div class="banner">
    <div class="banner__photo" role="img" aria-label="Foto: junge Frau mit rotbraunem Haar sitzt auf einem gepflasterten Weg und liest auf einem Tablet"></div>
    <div class="banner__fade"></div>

    <div class="brand">
      <span class="brand__name">veltrama</span>
      <span class="brand__tagline">FINANCE CONSULTING</span>
    </div>

    <h1 class="headline">Mehr Unabhängigkeit mit einem<br>persönlichen Finanzkonzept</h1>

    <ul class="benefits">
      <li class="benefits__item">
        <svg class="benefits__tick" viewBox="0 0 22 22" aria-hidden="true"><path d="M3 12 L8 18 L19 3" fill="none" stroke="#d0212b" stroke-width="3.6" stroke-linecap="round" stroke-linejoin="round"/></svg>
        Ganzheitliche Betrachtung Ihrer Finanzsituation
      </li>
      <li class="benefits__item">
        <svg class="benefits__tick" viewBox="0 0 22 22" aria-hidden="true"><path d="M3 12 L8 18 L19 3" fill="none" stroke="#d0212b" stroke-width="3.6" stroke-linecap="round" stroke-linejoin="round"/></svg>
        Nie mehr Kündigungstermine verpassen
      </li>
      <li class="benefits__item">
        <svg class="benefits__tick" viewBox="0 0 22 22" aria-hidden="true"><path d="M3 12 L8 18 L19 3" fill="none" stroke="#d0212b" stroke-width="3.6" stroke-linecap="round" stroke-linejoin="round"/></svg>
        Zahlen Sie nur soviel wie nötig
      </li>
    </ul>

    <a class="cta" href="#">JETZT ANFRAGEN</a>

    <div class="web-address">WWW.VELTRAMA.DE</div>
  </div>
</body>
</html>
```